Uncoded front page web design for wedding and event planning company

Hi.

I am launching a wedding and event planning company called Silver Fern Gatherings and need a professional and appealing web design.

So, let me explain my company. I am based in Swindon in Wiltshire but the company will plan weddings and events in Oxfordshire, Wiltshire, Berkshire and London.

We will plan weddings, birthdays, conferences, product launches, fashion shows and conventions but the main focus of the website at this stage should be the weddings with all the other occasions being covered under a single 'events' heading.

My contact details for the website should be:
Marion Blake
marion@silverferngatherings.co.uk
01632 960457 / 07700 900583

I'd like the website to feel clean, bright and elegant and be set against a white or off-white background. My logo is purple and I'd therefore like some purple incorporated into the design although feel free to use a more muted purple as my one might be a little bright? I'm also considering whether it would look nice paired with a little of the colour gold - maybe as a font colour in places?? I'll leave you to figure that one out as your design eye will be better than mine but for your reference below is my purple colour and my suggested gold one....

My purple colour is Pantone 2592 C but feel free to use others
My suggested gold I'm looking at is Pantone 14-1041 TCX

I would like to incorporate a Facebook feed in the front page if possible, if it looks right. I'd also like to include a variety of pictures as well so I've included a few in a Dropbox folder which is linked below. Please don't feel obliged to use them all by any means (there's loads!) but you've got a few there to play with. If you find any other royalty free images you'd rather use please go ahead but on the understanding I can have them afterwards!

My logo can be retrieved via this Dropbox link...
You'll notice there are 2 styles of placement. Please feel free to use either to fit in with your design...
https://www.filedrawer-example.com/sh/qk7pa2mwx9rn4lt/BBBKzq8ohPnvve4S03LoPjvb?dl=0

The wedding images I have are in this Dropbox folder...
https://www.filedrawer-example.com/sh/m8wd6rzp2lo4ye1/BBB4kqrXv8nWd7S05JmOgtlp?dl=0

Other than that, it's over to you.... I can't wait to receive your designs :-)

Ooh....finally just to say, as I receive designs in I think I'll notice aspects that I like and don't like and if I feel they'll be useful for other designers, I'll update my brief below. Thanks

BRIEF UPDATE:
Someone asked if I had a tag-line. Could you use "Creating exquisite occasions today for amazing memories tomorrow"

I realise I hadn't explained what I'd like included on my home page so here's some notes to consider....

A welcome to section for me to start narrative about us and our services which has a button that links to our 'about us' page and 'services' page for further information.

A section that nicely illustrates what services we offer whether that be with icons or pictures.

A section with some photos in that would link to our gallery

A section that shows some customer reviews and blog entries that would link to my reviews page and blog to read more.

And finally a contact us section with my details, social media links and site map.

***
I also need to draw attention to where in the UK my services cover. I was therefore thinking perhaps we could use a picture to demonstrate this where it highlights Wiltshire, Oxfordshire, Berkshire and London on a map thereby demonstrating our areas covered. I have found several English county maps when searching on Google but I'm not sure how to highlight the areas I cover (or dull out the areas I don't) so if you have any ideas on this, I'd really like it incorporated. Thanks. (by the way, for those of you not familiar with English counties, the ones I cover are often abbreviated to Wilts, Oxon, Berks, London, so if you find a suitable map with those names on rather than the full names, you'll know what they are!)

I've found an image of the county map which might work well. I was wondering whether we might somehow grey out the counties I don't cover and just keep the ones I do as mentioned above and then crop it into perhaps a shadowed circle? I've attached a screenshot to the brief.
Updates

I've decided on the tag-line "Creating exquisite occasions today for amazing memories tomorrow" so if that could be included somewhere that would be great. I also need to draw attention to where in the UK my services cover. I was therefore thinking perhaps we could use a picture to demonstrate this where it highlights Wiltshire, Oxfordshire, Berkshire and London on a map thereby demonstrating our areas covered. I have found several English county maps when searching on Google but I'm not sure how to highlight the areas I cover (or dull out the areas I don't) so if you have any ideas on this, I'd really like it incorporated. Thanks. Added Wednesday, June 24, 2015

Target Market(s)

Predominately women aged 25-55

Industry/Entity Type

Wedding Planner

Number of Pages Required

1 page

Font styles to use
Sans Serif
Script

Requirements
Nice to have
• I'd like to see how the colour theme of purple and perhaps a little gold (maybe as a font colour) look against a white background. I've mentioned the Pantone colours in the brief above.
• I've attached a screenshot of a webpage with gold writing in and fonts that I like. Perhaps it could give you inspiration?
Should not have
• I really don't like the font QUILLORA so please done use that.

```html
<!DOCTYPE html>
<html lang="en">
<head>
<meta charset="utf-8">
<title>Silver Fern Gatherings</title>
<link rel="stylesheet" href="https://fonts.googleapis.com/css2?family=Parisienne&family=Playfair+Display:ital,wght@1,700&family=Open+Sans:wght@400;600&display=swap">
<style>
:root{
  --cream:#f6efe0;
  --cream-deep:#efe3cb;
  --paper:#fbf7ee;
  --gold:#b8925a;
  --gold-dark:#8e6b3a;
  --purple:#9a3f9a;
  --text:#5a4a3a;
  --footer:#2b2724;
  --footer-text:#d9cfbf;
  --line:#dccbab;
}
*{margin:0;padding:0;box-sizing:border-box}
html,body{width:1200px;height:2520px;overflow:hidden}
body{background:var(--paper);font-family:"Open Sans",sans-serif;color:var(--text);position:relative}

.site-header{position:absolute;top:0;left:0;width:1200px;height:220px;background:var(--cream)}
.brand{position:absolute;top:38px;left:0;width:1200px;display:flex;justify-content:center;align-items:center;gap:16px}
.brand-dot{width:46px;height:46px;border-radius:50%;background:var(--purple)}
.brand-name{font-family:"Parisienne",cursive;font-size:52px;color:var(--purple)}
.main-nav{position:absolute;top:172px;left:0;width:1200px;display:flex;justify-content:center;gap:44px;font-size:17px;letter-spacing:1px;text-transform:uppercase}
.main-nav a{color:var(--text);text-decoration:none;padding-bottom:8px}
.main-nav a.active{color:var(--gold);border-bottom:2px solid var(--gold)}

.hero{position:absolute;top:220px;left:0;width:1200px;height:540px;background:linear-gradient(90deg,#7a5a3e,#c9a589 30%,#e7d2c7 55%,#b98b7d 80%,#6e5140)}
.hero-circle{position:absolute;left:420px;top:90px;width:360px;height:360px;border-radius:50%;background:rgba(255,255,255,.55);border:3px solid rgba(255,255,255,.85);display:flex;flex-direction:column;justify-content:center;align-items:center;text-align:center;color:#4a3527}
.hero-script{font-family:"Parisienne",cursive;font-size:44px;line-height:1.05}
.hero-bold{font-family:"Playfair Display",serif;font-style:italic;font-weight:700;font-size:40px;line-height:1.2}

.welcome{position:absolute;top:760px;left:0;width:1200px;height:700px;background:var(--cream)}
.section-title{font-family:"Parisienne",cursive;color:var(--gold);font-size:62px;text-align:center}
.welcome .section-title{margin-top:40px}
.lead{width:760px;margin:18px auto 0;text-align:center;font-size:14px;line-height:1.6}
.services{position:absolute;top:250px;left:100px;width:1000px;display:flex;justify-content:space-between}
.service{width:300px;text-align:center}
.service-photo{width:200px;height:200px;border-radius:50%;margin:0 auto;border:6px solid #fff;box-shadow:0 0 0 2px var(--line)}
.service h3{font-family:"Parisienne",cursive;color:var(--gold);font-weight:400;font-size:40px;margin-top:22px}
.service p{font-size:14px;line-height:1.6;margin-top:8px}
.divider{position:absolute;top:650px;left:100px;width:1000px;height:2px;background:var(--line)}
.divider-badge{position:absolute;left:460px;top:-38px;width:80px;height:80px;border-radius:50%;background:var(--gold);border:4px solid var(--cream-deep)}

.portfolio{position:absolute;top:1460px;left:0;width:1200px;height:460px;background:var(--cream)}
.portfolio .section-title{margin-top:40px}
.gallery{position:absolute;top:175px;left:75px;width:1050px;display:flex;justify-content:space-between}
.gallery-item{width:330px;height:220px;border:5px solid #fff;box-shadow:0 0 0 2px var(--line)}
.gallery-text{display:flex;align-items:center;justify-content:center;background:linear-gradient(135deg,#c9a66a,#e3c690,#b48e52);font-family:"Playfair Display",serif;font-style:italic;font-weight:700;font-size:28px;color:#4a3527;text-align:center;padding:30px}
.arrow{position:absolute;top:265px;width:40px;height:80px;background:#d8d2c8;display:flex;align-items:center;justify-content:center}
.arrow-left{left:0;border-radius:0 40px 40px 0}
.arrow-right{right:0;border-radius:40px 0 0 40px}

.subscribe{position:absolute;top:1920px;left:0;width:1200px;height:380px;background:linear-gradient(90deg,#f1e3c6,#f8efdc 40%,#f3e3cc 70%,#ead0bd)}
.subscribe .section-title{margin-top:60px}
.subscribe .lead{width:900px}
.sub-form{position:absolute;top:255px;left:100px;display:flex;gap:42px;align-items:center}
.sub-input{width:360px;height:44px;border:1px solid var(--line);background:#fff;border-radius:4px;font-size:13px;color:#a89a88;padding:12px 16px}
.sub-button{width:180px;height:48px;border-radius:24px;background:var(--gold);color:#fff;font-size:20px;display:flex;align-items:center;justify-content:center}

.site-footer{position:absolute;top:2300px;left:0;width:1200px;height:220px;background:var(--footer);color:var(--footer-text)}
.footer-nav{position:absolute;top:50px;left:0;width:1200px;display:flex;justify-content:center;gap:36px;font-size:17px}
.footer-nav span{padding:6px 26px}
.footer-nav .active{border:1px solid var(--footer-text);border-radius:20px}
.footer-bar{position:absolute;top:130px;left:0;width:1200px;height:90px;border-top:1px solid #3f3a35;display:flex;align-items:center;padding:0 70px;font-size:14px}
.contact{display:flex;align-items:center;gap:14px;margin-right:60px}
.contact-icon{width:40px;height:40px;border-radius:50%;background:var(--gold);display:flex;align-items:center;justify-content:center}
.copyright{margin-left:auto;font-size:13px}
</style>
</head>
<body>
<header class="site-header">
  <div class="brand"><span class="brand-dot"></span><span class="brand-name">Silver Fern Gatherings</span></div>
  <nav class="main-nav">
    <a class="active">Home</a><a>About</a><a>Services</a><a>Course</a><a>Shop</a><a>Contact</a>
  </nav>
</header>

<section class="hero" role="img" aria-label="Candle-lit wedding table with flower arrangements">
  <div class="hero-circle">
    <div class="hero-script">Creating<br>Exquisite Occasions<br>Today For</div>
    <div class="hero-bold">Amazing Memories</div>
    <div class="hero-script">Tomorrow</div>
  </div>
</section>

<section class="welcome">
  <h2 class="section-title">Welcome to Silver Fern</h2>
  <p class="lead">Lorem Ipsum is simply dummy text of the printing and typesetting industry. Lorem Ipsum has been the industry's standard dummy text ever since the 1500s, when an unknown printer took a galley of type and scrambled it to make a type specimen book.</p>
  <div class="services">
    <div class="service">
      <div class="service-photo" role="img" aria-label="Wedding ceremony aisle" style="background:radial-gradient(circle,#e9dfe4,#b79aa8)"></div>
      <h3>Full Planning</h3>
      <p>Lorem Ipsum is simply dummy text of the printing and typesetting industry. Lorem Ipsum has been the industry.</p>
    </div>
    <div class="service">
      <div class="service-photo" role="img" aria-label="Purple floral table styling" style="background:radial-gradient(circle,#c9a9d6,#6e4a80)"></div>
      <h3>Styling</h3>
      <p>Lorem Ipsum is simply dummy text of the printing and typesetting industry. Lorem Ipsum has been the industry.</p>
    </div>
    <div class="service">
      <div class="service-photo" role="img" aria-label="Wedding budget checklist" style="background:radial-gradient(circle,#fbf6f2,#d9b7b3)"></div>
      <h3>Budget</h3>
      <p>Lorem Ipsum is simply dummy text of the printing and typesetting industry. Lorem Ipsum has been the industry.</p>
    </div>
  </div>
  <div class="divider"><span class="divider-badge"></span></div>
</section>

<section class="portfolio">
  <h2 class="section-title">Our Portfolio</h2>
  <div class="gallery">
    <div class="gallery-item" role="img" aria-label="Bride's dress being laced" style="background:linear-gradient(135deg,#6b5444,#e8ded6 50%,#8d7462)"></div>
    <div class="gallery-item gallery-text">Lorem Ipsum is simply dummy text!</div>
    <div class="gallery-item" role="img" aria-label="Reception table with flowers and candles" style="background:linear-gradient(135deg,#2e2622,#c8a48f 50%,#3a2f29)"></div>
  </div>
  <div class="arrow arrow-left"><svg width="14" height="24" viewBox="0 0 14 24"><path d="M12 2 2 12l10 10" fill="none" stroke="#fff" stroke-width="3"/></svg></div>
  <div class="arrow arrow-right"><svg width="14" height="24" viewBox="0 0 14 24"><path d="M2 2l10 10L2 22" fill="none" stroke="#fff" stroke-width="3"/></svg></div>
</section>

<section class="subscribe">
  <h2 class="section-title">Subscribe to Silver Fern</h2>
  <p class="lead">Lorem Ipsum is simply dummy text of the printing and typesetting industry. Lorem Ipsum has been the industry's standard dummy text ever since the 1500s, when an unknown printer took a galley of type and scrambled it to make a type specimen book.</p>
  <div class="sub-form">
    <div class="sub-input">Enter your name</div>
    <div class="sub-input">Enter your email</div>
    <div class="sub-button">Subscribe</div>
  </div>
</section>

<footer class="site-footer">
  <nav class="footer-nav">
    <span class="active">Home</span><span>About</span><span>Service</span><span>Course</span><span>Shop</span><span>Contact</span>
  </nav>
  <div class="footer-bar">
    <div class="contact">
      <span class="contact-icon"><svg width="18" height="18" viewBox="0 0 24 24"><rect x="6" y="2" width="12" height="20" rx="2" fill="none" stroke="#fff" stroke-width="2"/><circle cx="12" cy="18" r="1.3" fill="#fff"/></svg></span>
      <span>01632 960457<br>07700 900583</span>
    </div>
    <div class="contact">
      <span class="contact-icon"><svg width="18" height="18" viewBox="0 0 24 24"><rect x="2" y="5" width="20" height="14" fill="none" stroke="#fff" stroke-width="2"/><path d="M2 5l10 8 10-8" fill="none" stroke="#fff" stroke-width="2"/></svg></span>
      <span>marion@silverferngatherings.co.uk</span>
    </div>
    <span class="copyright">© Silver Fern Gatherings - 2015. All Rights Reserved</span>
  </div>
</footer>
</body>
</html>
```